TallonCryo Website - Biologics storage and handling

I would like a beginning design on a website for TallonCryo:

A Boston-based company dedicated to sourcing, storing, and supplying biologic materials of all kinds to the life sciences and scientific markets. From starting reagents, to basic and intermediate materials, to final synthesized and engineered products, we provide value throughout the biologics supply chain. TallonCryo provides backup, overflow, emergency, and stocking storage solutions to companies on a temporary or permanent basis. Life sciences companies can take advantage of the fact that the company is located in the middle of the Boston/Cambridge biotechnology corridor in order to have quick and efficient access to their cold chain materials. Out of state companies can leverage TallonCryo’s location for efficient distribution of materials to partner and client organizations. We also provide other value added services to organizations that do not have the local manpower, such as sourcing, supply, and distribution of materials.

The design should be mostly a white background with clean, linear, geometric colors added in according to the blue and orange color scheme represented in the corporate logo attached.

The website needs to communicate reliable service and provide the concept of a company dedicated to handling and providing client biological samples in a secure and efficient manner.

Some local competitors are:
1. Orlen BioServices: www.orlenbio-example.com
2. VaultiCore: www.vaulticore-example.com

From a design perspective, I like the Meridel Thera website:

www.merideltheraexample.com

Target Market(s)

Life sciences companies and other organizations

Industry/Entity Type

Biotechnology

Coding

Coded - Design and coding required

Number of Pages Required

5+ page

Font styles to use
Sans Serif

Colors
3176b5
0455a3
f37122

Requirements
Must have
• Tabs for pages:
About - Company information.
Platform - Inventory and sample management cloud platform; temperature profiling, logging, and reporting.
Services - Refrigeration and freezing services for biological samples, logistics services, sourcing services, courier services.
Updates - News, events, blog.
Login portal - Entry point for getting into platform. Maybe some freemium content here.
Nice to have
• Please be creative about website page sections, vibrant colors according to my established color scheme, and clean, linear, geometric shapes. I would like a white background with nice colors, clean lines and borders, and a very contemporary look. I want o
Should not have
• This is not a Business to Consumer business. This is a Business to Business enterprise. There should not be consumer oriented language. It is more about service and relationship management.

```html
<!DOCTYPE html>
<html lang="en">
<head>
<meta charset="utf-8">
<title>TallonCryo — Biologics Storage and Handling</title>
<link href="https://fonts.googleapis.com/css2?family=Raleway:wght@400;500;600;700&family=Montserrat:wght@400;500;600&display=swap" rel="stylesheet">
<style>
:root{
  --orange:#e0601f;
  --orange-light:#f37122;
  --navy:#1f4e64;
  --teal-dark:#285868;
  --teal-button:#245a6b;
  --blue:#3176b5;
  --grey-bg:#f5f5f5;
  --text:#555;
  --white:#fff;
}
*{margin:0;padding:0;box-sizing:border-box}
html,body{width:1200px;height:3620px;overflow:hidden;background:var(--white)}
body{position:relative;font-family:Arial,Helvetica,sans-serif;color:var(--text)}
.abs{position:absolute}
.center{text-align:center}

/* header */
.site-header{position:absolute;left:0;top:0;width:1200px;height:142px;background:var(--white)}
.brand{position:absolute;left:110px;top:50px;display:flex;align-items:center;gap:12px;font-family:Raleway,sans-serif;font-weight:500;font-size:31px;color:var(--navy)}
.brand-mark{width:22px;height:22px;background:var(--orange)}
.top-action{position:absolute;top:24px;display:flex;align-items:center;gap:8px;font-family:Raleway,sans-serif;font-size:16px;color:var(--orange)}
.top-action .dot{width:48px;height:48px;border-radius:50%;background:var(--orange);display:flex;align-items:center;justify-content:center}
.main-nav{position:absolute;top:99px;left:438px;display:flex;gap:0;font-family:Raleway,sans-serif;font-size:15px;font-weight:500;color:#333}
.main-nav span{margin-right:40px}
.main-nav .active{color:var(--orange)}

/* hero */
.hero{position:absolute;left:0;top:142px;width:1200px;height:648px}
.hero-title{position:absolute;left:108px;top:218px;font-family:Raleway,sans-serif;font-weight:500;font-size:66px;line-height:1;color:var(--white);letter-spacing:1px;text-shadow:0 2px 4px rgba(0,0,0,.25)}
.hero-text{position:absolute;left:111px;top:315px;width:480px;font-size:16px;line-height:27px;color:#eef3f8}
.btn-solid{position:absolute;background:linear-gradient(#e8692a,#d4521a);color:var(--white);font-family:Raleway,sans-serif;font-size:16px;font-weight:500;display:flex;align-items:center;justify-content:center;border-radius:3px}

/* section titles */
.section-title{position:absolute;left:0;width:1200px;text-align:center;font-family:Raleway,sans-serif;font-weight:500;font-size:39px;color:var(--navy)}
.section-title em{font-style:normal;color:var(--orange)}
.rule{position:absolute;left:571px;width:58px;height:3px;background:var(--orange)}

.about-text{position:absolute;left:190px;width:820px;text-align:center;font-size:13px;line-height:25px;color:#444}

/* platform */
.platform{position:absolute;left:0;top:1245px;width:1200px;height:460px;background:var(--grey-bg)}
.plat-card{position:absolute;top:153px;width:225px;height:225px;background:var(--white);border:1px solid var(--orange);text-align:center}
.plat-card.blue{border-color:var(--blue)}
.plat-card svg{position:absolute;left:80px;top:28px}
.plat-card p{position:absolute;left:10px;right:10px;top:122px;font-family:Montserrat,sans-serif;font-weight:500;font-size:15px;line-height:26px;color:var(--orange)}
.plat-card.blue p{color:var(--navy)}

/* blog */
.blog-img{position:absolute;top:1834px;width:311px;height:248px}
.blog-card{position:absolute;top:2026px;width:276px;height:264px;background:var(--white);box-shadow:0 2px 6px rgba(0,0,0,.12);text-align:center}
.blog-card h3{margin-top:32px;font-family:Raleway,sans-serif;font-weight:600;font-size:19px;color:#333}
.blog-card .date{margin-top:12px;font-family:Montserrat,sans-serif;font-weight:600;font-size:16px;color:var(--orange)}
.blog-card p{margin:14px 22px 0;font-size:13px;line-height:26px;color:#555}
.btn-outline{display:inline-block;margin-top:16px;padding:0 14px;height:39px;line-height:37px;border:1px solid var(--orange);color:var(--orange);font-family:Montserrat,sans-serif;font-weight:600;font-size:13px;border-radius:2px}

/* services */
.services{position:absolute;left:0;top:2350px;width:1200px;height:486px;background:linear-gradient(180deg,#f7f7f7,#efefef)}
.svc{position:absolute;top:162px;width:220px;text-align:center}
.svc .ring{width:126px;height:126px;margin:0 auto;border-radius:50%;border:2px solid var(--orange);background:var(--white);display:flex;align-items:center;justify-content:center}
.svc .ring.blue{border-color:var(--navy)}
.svc h4{margin-top:18px;font-family:Montserrat,sans-serif;font-weight:600;font-size:17px;line-height:25px;color:#333;letter-spacing:.5px}
.svc p{margin-top:10px;font-size:13px;line-height:25px;color:#666}

/* newsletter */
.newsletter{position:absolute;left:0;top:2836px;width:1200px;height:397px;background:linear-gradient(120deg,#e26521,#d9581b 60%,#e16b2a)}
.newsletter .section-title{color:var(--white)}
.news-text{position:absolute;left:200px;width:800px;top:150px;text-align:center;font-size:16px;line-height:30px;color:#fde9dc}
.email-field{position:absolute;left:259px;top:218px;width:717px;height:54px;border:1.5px solid var(--white);border-radius:3px;color:var(--white);font-size:12px;padding:20px 0 0 18px}
.submit{position:absolute;left:512px;top:290px;width:176px;height:52px;background:var(--teal-button);color:var(--white);font-family:Raleway,sans-serif;font-size:18px;font-weight:500;display:flex;align-items:center;justify-content:center;border-radius:3px}

/* footer */
.site-footer{position:absolute;left:0;top:3233px;width:1200px;height:387px;background:var(--teal-dark);color:var(--white)}
.footer-brand{position:absolute;left:120px;top:170px;display:flex;align-items:center;gap:14px;font-family:Raleway,sans-serif;font-weight:500;font-size:44px;color:var(--white)}
.footer-brand .brand-mark{width:30px;height:30px;background:var(--white)}
.footer-col h5{position:absolute;top:54px;font-family:Montserrat,sans-serif;font-weight:500;font-size:19px;color:var(--white)}
.quick li{list-style:none;position:absolute;left:454px;font-family:Montserrat,sans-serif;font-weight:600;font-size:12px;display:flex;align-items:center;gap:10px}
.quick li i{display:inline-block;width:16px;height:1px;background:var(--white);position:relative}
.quick li i:after{content:"";position:absolute;right:0;top:-3px;border-left:5px solid var(--white);border-top:3.5px solid transparent;border-bottom:3.5px solid transparent}
.contact-row{position:absolute;left:643px;display:flex;align-items:center;gap:12px;font-family:Montserrat,sans-serif;font-size:13px}
.contact-row .c{width:34px;height:34px;border-radius:50%;background:#3e6a79;display:flex;align-items:center;justify-content:center;flex:none}
.follow-row{position:absolute;left:922px;display:flex;align-items:center;gap:10px;font-family:Montserrat,sans-serif}
.follow-row .d{width:36px;height:36px;background:var(--white);transform:rotate(45deg);flex:none;margin:0 4px}
.follow-row small{display:block;font-size:11px;color:#cfdde2}
.follow-row span{font-size:15px}
.copyright{position:absolute;left:0;width:1200px;top:347px;text-align:center;font-size:13px;color:#dfe9ec}
</style>
</head>
<body>

<header class="site-header">
  <div class="brand"><span class="brand-mark"></span>TallonCryo</div>
  <div class="top-action" style="left:696px">
    <span class="dot"><svg width="16" height="18" viewBox="0 0 16 18"><circle cx="8" cy="5" r="4" fill="#fff"/><path d="M1 17c0-5 3-7 7-7s7 2 7 7z" fill="#fff"/></svg></span>LOGIN
  </div>
  <div class="top-action" style="left:829px">
    <span class="dot"><svg width="18" height="18" viewBox="0 0 24 24"><path d="M6.6 10.8a15 15 0 006.6 6.6l2.2-2.2a1 1 0 011-.25 11 11 0 003.6.6 1 1 0 011 1V20a1 1 0 01-1 1A17 17 0 013 4a1 1 0 011-1h3.5a1 1 0 011 1 11 11 0 00.6 3.6 1 1 0 01-.25 1z" fill="#fff"/></svg></span>CALL US : 000-555-0142
  </div>
  <nav class="main-nav">
    <span class="active">HOME</span><span>ABOUT</span><span>PLATFORM</span><span>SERVICES</span><span>NEWS</span><span>CONTACT US</span>
  </nav>
</header>

<section class="hero">
  <svg class="abs" style="left:0;top:0" width="1200" height="648" role="img" aria-label="Photo of a gloved hand opening a laboratory freezer door, blue-toned">
    <defs>
      <linearGradient id="heroGrad" x1="0" y1="0" x2="1" y2="1">
        <stop offset="0" stop-color="#6d8fb7"/>
        <stop offset=".5" stop-color="#8fabcc"/>
        <stop offset="1" stop-color="#5d7fa9"/>
      </linearGradient>
    </defs>
    <polygon points="0,0 1200,0 1200,555 600,648 0,555" fill="url(#heroGrad)"/>
  </svg>
  <h1 class="hero-title">TALLONCRYO</h1>
  <p class="hero-text">Sed ut perspiciatis unde omnis iste natus error sit voluptatem accusantium doloremque laudantium</p>
  <div class="btn-solid" style="left:111px;top:391px;width:142px;height:50px">READ MORE</div>
</section>

<h2 class="section-title" style="top:848px">ABOUT <em>TALLONCRYO</em></h2>
<div class="rule" style="top:912px"></div>
<p class="about-text" style="top:941px">A Boston-based company dedicated to sourcing, storing, and supplying biologic materials of all kinds to the life sciences and scientific markets. From starting reagents, to basic and intermediate materials, to final synthesized and engineered products, we provide value throughout the biologics supply chain. TallonCryo provides backup, overflow, emergency, and stocking storage solutions to companies on a temporary or permanent basis.</p>
<p class="about-text" style="top:1066px">Life sciences companies can take advantage of the fact that the company is located in the middle of the Boston/Cambridge biotechnology corridor in order to have quick and efficient access to their cold chain materials.</p>
<div class="btn-solid" style="left:515px;top:1143px;width:170px;height:48px">READ MORE</div>

<section class="platform">
  <h2 class="section-title" style="top:60px"><em>PLATFORM</em></h2>
  <div class="rule" style="top:112px"></div>
  <div class="plat-card blue" style="left:112px">
    <svg width="66" height="66" viewBox="0 0 66 66" fill="none" stroke="#1f4e64" stroke-width="2"><path d="M16 38a10 10 0 010-20 14 14 0 0127-4 11 11 0 017 24z"/><path d="M22 38v12M30 38v16M38 38v16M46 38v12"/><circle cx="22" cy="53" r="3"/><circle cx="30" cy="57" r="3"/><circle cx="38" cy="57" r="3"/><circle cx="46" cy="53" r="3"/></svg>
    <p>Inventory and sample management cloud platform</p>
  </div>
  <div class="plat-card" style="left:362px">
    <svg width="66" height="66" viewBox="0 0 66 66" fill="none" stroke="#e0601f" stroke-width="2"><path d="M28 6a5 5 0 0110 0v36a10 10 0 11-10 0z"/><circle cx="33" cy="50" r="5" fill="#e0601f"/><path d="M33 20v25"/></svg>
    <p>Temperature Profiling</p>
  </div>
  <div class="plat-card blue" style="left:613px">
    <svg width="66" height="66" viewBox="0 0 66 66" fill="none" stroke="#1f4e64" stroke-width="2"><rect x="6" y="4" width="54" height="58" rx="3"/><path d="M6 12h54"/><circle cx="33" cy="28" r="7"/><path d="M22 44h22M20 50h26M20 56h26"/></svg>
    <p>Logging</p>
  </div>
  <div class="plat-card" style="left:864px">
    <svg width="66" height="66" viewBox="0 0 66 66" fill="none" stroke="#e0601f" stroke-width="2"><rect x="8" y="44" width="7" height="16"/><rect x="22" y="36" width="7" height="24"/><rect x="36" y="40" width="7" height="20"/><rect x="50" y="28" width="7" height="32"/><path d="M11 30l14-10 14 8 14-16"/><circle cx="11" cy="30" r="3"/><circle cx="25" cy="20" r="3"/><circle cx="39" cy="28" r="3"/><circle cx="53" cy="12" r="3"/></svg>
    <p>Reporting</p>
  </div>
</section>

<h2 class="section-title" style="top:1740px">LATEST <em>BLOG</em></h2>
<div class="rule" style="top:1800px"></div>

<svg class="blog-img" style="left:112px" role="img" aria-label="Gloved hand holding a sample vial with tweezers"><defs><linearGradient id="b1" x1="0" y1="0" x2="1" y2="1"><stop offset="0" stop-color="#eef2f6"/><stop offset=".6" stop-color="#b5c6d8"/><stop offset="1" stop-color="#4f78a8"/></linearGradient></defs><rect width="311" height="248" fill="url(#b1)"/></svg>
<svg class="blog-img" style="left:444px" role="img" aria-label="Technician handling blood sample tubes beside a laptop"><defs><linearGradient id="b2" x1="0" y1="0" x2="1" y2="1"><stop offset="0" stop-color="#6d6f73"/><stop offset=".5" stop-color="#c8c9cb"/><stop offset="1" stop-color="#6fa6d4"/></linearGradient></defs><rect width="311" height="248" fill="url(#b2)"/></svg>
<svg class="blog-img" style="left:776px" role="img" aria-label="Rack of blue test tubes in a laboratory"><defs><linearGradient id="b3" x1="0" y1="0" x2="1" y2="1"><stop offset="0" stop-color="#e8f2f8"/><stop offset=".5" stop-color="#8fc3e4"/><stop offset="1" stop-color="#3a8fc8"/></linearGradient></defs><rect width="311" height="248" fill="url(#b3)"/></svg>

<article class="blog-card" style="left:130px"><h3>SED UT PERSPICIA</h3><div class="date">08 JUNE 2020</div><p>Nemo enim ipsam voluptatem quia voluptas sit aspernatur aut odit aut sed quia consequuntur</p><span class="btn-outline">READ MORE</span></article>
<article class="blog-card" style="left:462px"><h3>SED UT PERSPICIA</h3><div class="date">08 JUNE 2020</div><p>Nemo enim ipsam voluptatem quia voluptas sit aspernatur aut odit aut sed quia consequuntur</p><span class="btn-outline">READ MORE</span></article>
<article class="blog-card" style="left:794px"><h3>SED UT PERSPICIA</h3><div class="date">08 JUNE 2020</div><p>Nemo enim ipsam voluptatem quia voluptas sit aspernatur aut odit aut sed quia consequuntur</p><span class="btn-outline">READ MORE</span></article>

<section class="services">
  <h2 class="section-title" style="top:50px">OUR <em>SERVICES</em></h2>
  <div class="rule" style="top:113px"></div>
  <div class="svc" style="left:123px">
    <div class="ring"><svg width="70" height="70" viewBox="0 0 70 70" fill="none" stroke="#e0601f" stroke-width="4" stroke-linecap="round"><path d="M35 6v58M10 20l50 30M10 50l50-30"/><path d="M28 10l7 6 7-6M28 60l7-6 7 6M8 30l9 2-2-9M62 40l-9-2 2 9M8 40l9-2-2 9M62 30l-9 2 2-9"/></svg></div>
    <h4>REFRIGERATION &amp;<br>FREEZING</h4>
    <p>Sed ut perspiciatis unde omnis iste natus error sit voluptatem acc usantium dolorem</p>
  </div>
  <div class="svc" style="left:369px">
    <div class="ring blue"><svg width="74" height="60" viewBox="0 0 74 60" fill="none" stroke="#1f4e64" stroke-width="2"><rect x="4" y="8" width="42" height="36"/><path d="M46 20h14l10 12v12H46z"/><circle cx="18" cy="48" r="6"/><circle cx="58" cy="48" r="6"/><path d="M10 18h28M10 26h20M10 34h24"/></svg></div>
    <h4>LOGISTICS<br>SERVICES</h4>
    <p>Sed ut perspiciatis unde omnis iste natus error sit voluptatem acc usantium dolorem</p>
  </div>
  <div class="svc" style="left:615px">
    <div class="ring"><svg width="74" height="70" viewBox="0 0 74 70" fill="none" stroke="#e0601f" stroke-width="2"><path d="M28 22a7 7 0 010-14 9 9 0 0117-1 7 7 0 012 15z"/><path d="M36 22v14M20 36h34"/><circle cx="16" cy="52" r="11"/><path d="M5 52h22M16 41c-6 7-6 15 0 22M16 41c6 7 6 15 0 22"/><rect x="40" y="40" width="24" height="16"/><path d="M36 60h32"/></svg></div>
    <h4>SOURCING<br>SERVICES</h4>
    <p>Sed ut perspiciatis unde omnis iste natus error sit voluptatem acc usantium dolorem</p>
  </div>
  <div class="svc" style="left:860px">
    <div class="ring blue"><svg width="70" height="70" viewBox="0 0 70 70" fill="none" stroke="#1f4e64" stroke-width="2"><rect x="6" y="6" width="44" height="40"/><path d="M6 22h44M28 6v40"/><rect x="28" y="36" width="36" height="26"/><path d="M28 36l18 14 18-14M28 62l14-12M64 62l-14-12"/><path d="M16 50V32M10 38l6-6 6 6"/></svg></div>
    <h4>COURIER<br>SERVICES</h4>
    <p>Sed ut perspiciatis unde omnis iste natus error sit voluptatem acc usantium dolorem</p>
  </div>
</section>

<section class="newsletter">
  <h2 class="section-title" style="top:52px">NEWSLETTER SIGNUP</h2>
  <div class="rule" style="top:110px;background:#fff"></div>
  <p class="news-text">Sed ut perspiciatis unde omnis iste natus error sit voluptatem accusantium doloremque laudantium eaque ipsa quae ab illo inventore veritatis et quasi</p>
  <div class="email-field">Enter Your Email id :</div>
  <div class="submit">SUBMIT</div>
</section>

<footer class="site-footer">
  <div class="footer-brand"><span class="brand-mark"></span>TallonCryo</div>
  <div class="footer-col"><h5 style="left:454px">QUICK LINKS</h5><h5 style="left:645px">CONTACT US</h5><h5 style="left:928px">FOLLOW US</h5></div>
  <ul class="quick">
    <li style="top:105px"><i></i>HOME</li>
    <li style="top:132px"><i></i>ABOUT US</li>
    <li style="top:160px"><i></i>PLATFORM</li>
    <li style="top:187px"><i></i>SERVICES</li>
    <li style="top:215px"><i></i>NEWS</li>
    <li style="top:242px"><i></i>CONTACT US</li>
  </ul>
  <div class="contact-row" style="top:102px"><span class="c"><svg width="14" height="14" viewBox="0 0 24 24"><path d="M6.6 10.8a15 15 0 006.6 6.6l2.2-2.2a1 1 0 011-.25 11 11 0 003.6.6 1 1 0 011 1V20a1 1 0 01-1 1A17 17 0 013 4a1 1 0 011-1h3.5a1 1 0 011 1 11 11 0 00.6 3.6 1 1 0 01-.25 1z" fill="#fff"/></svg></span>000.555.0142</div>
  <div class="contact-row" style="top:151px"><span class="c"><svg width="14" height="12" viewBox="0 0 14 12" fill="none" stroke="#fff" stroke-width="1.4"><rect x="1" y="1" width="12" height="10"/><path d="M1 1l6 5 6-5"/></svg></span>info@talloncryo-example.com</div>
  <div class="contact-row" style="top:191px;line-height:20px"><span class="c"><svg width="12" height="16" viewBox="0 0 12 16"><path d="M6 0a6 6 0 016 6c0 4-6 10-6 10S0 10 0 6a6 6 0 016-6z" fill="#fff"/><circle cx="6" cy="6" r="2" fill="#3e6a79"/></svg></span>#154 Lorem Ipsum Dummy text<br>Lorem Ipsum dummy</div>
  <div class="follow-row" style="top:97px"><span class="d"></span><div><small>Like us on</small><span>Socialpage</span></div></div>
  <div class="follow-row" style="top:155px"><span class="d"></span><div><small>Follow us on</small><span>Chirpline</span></div></div>
  <div class="follow-row" style="top:212px"><span class="d"></span><div><small>Follow us on</small><span>ProNet</span></div></div>
  <p class="copyright">© Copyrights 2020-TallonCryo.All Rights Reserved.</p>
</footer>

</body>
</html>
```